Business Card Design for a Jockey's Agent

A business card design that helps to develop a brand or identity for myself, the agent, perhaps on one side with a clean minimalist design, and on the other side a simple design with the two jockeys names i currently represent. Those jockeys may change twice a year as they move around the country, switch agents, etc, so i think keeping one side designed to promote the agent and a second side that can be changed easily to identify the jockeys i currently represent would be the best.

Target Market(s)

Thoroughbred racehorse trainers

Industry/Entity Type

Business

Contact Information for Business Card

Garrett Lindqvist - Jockey Agent
mobile (614) 382 7291
garrettplindqvist7mailhub.example

Jockeys: Everett Kline, Tobias Renwick

Font styles to use
Serif

Requirements
Must have
• contact info and modern feel and font
Nice to have
• clean minimalist element of racing, jockey silk, helmut or crop, finish marker pole from racetrack etc,
Should not have
• DONT HAVE ANY KIND OF LOGO ETC. IMAGE IS ONE OF MY RACEHORSES TO HELP FINISH BRIEF.
• racing horse, stuffy vintage racing feel or Weekly Paddock Sheet fonts

```html
<!DOCTYPE html>
<html lang="en">
<head>
<meta charset="UTF-8">
<title>Garrett Lindqvist — Jockey Agent</title>
<link rel="stylesheet" href="https://fonts.googleapis.com/css2?family=Cormorant+Garamond:wght@500;600&display=swap">
<style>
  :root {
    --paper: #ffffff;
    --frame: #111111;
    --ink: #2f383b;
    --ink-soft: #4f5b5e;
  }
  * { margin: 0; padding: 0; box-sizing: border-box; }
  html, body {
    width: 1200px;
    height: 686px;
    overflow: hidden;
    background: var(--paper);
  }
  .card {
    position: relative;
    width: 1200px;
    height: 686px;
    background: var(--paper);
    font-family: "Cormorant Garamond", Georgia, serif;
  }
  .card__frame {
    position: absolute;
    inset: 0;
  }
  .card__text {
    position: absolute;
    left: 0;
    width: 100%;
    text-align: center;
    white-space: nowrap;
    text-transform: uppercase;
  }
  .card__role {
    top: 274px;
    font-size: 30px;
    font-weight: 500;
    letter-spacing: 5px;
    color: var(--ink-soft);
  }
  .card__name {
    top: 318px;
    font-size: 44px;
    font-weight: 500;
    letter-spacing: 5px;
    color: var(--ink);
  }
  .card__contact {
    font-size: 18px;
    font-weight: 600;
    letter-spacing: 1.8px;
    color: var(--ink);
  }
  .card__contact--email { top: 374px; }
  .card__contact--mobile { top: 403px; }
  .card__contact-value { text-transform: none; }
</style>
</head>
<body>
  <main class="card">
    <svg class="card__frame" width="1200" height="686" viewBox="0 0 1200 686" aria-hidden="true">
      <polygon points="623,199 960,290 960,391 623,481 285,391 285,290"
               fill="none" stroke="var(--frame)" stroke-width="2"/>
    </svg>
    <p class="card__text card__role">Jockey Agent</p>
    <h1 class="card__text card__name">Garrett Lindqvist</h1>
    <p class="card__text card__contact card__contact--email">Email: <span class="card__contact-value">garrettplindqvist7mailhub.example</span></p>
    <p class="card__text card__contact card__contact--mobile">Mobile: <span class="card__contact-value">(614) 382 7291</span></p>
  </main>
</body>
</html>
```